Velsori Biotechnology needs a professional powerpoint design

We would like to re-design our powerpoint template(as attachment 1), it should be based on our current logo (as attachment 2). We hope the new powerpoint template could be more professional and like a biotechnology company with advanced technology.
Velsori Biotechnology is a contract development and manufacturing organization to provide high quality services to our clients in development, lead-in advanced technology and cGMP manufacturing of biopharmaceuticals from clinical to commercial manufacturing. We offers the advanced technology and services to become the best partner for clients from clinical to commercial manufacturing.
Reason: We would like to extend the deadline for this project so that designers can have more time to prepare, thanks.
Target Market(s)
Velsori Biotechnology is a contract development and manufacturing organization to provide high quality services to our clients in development, lead-in advanced technology and cGMP manufacturing of biopharmaceuticals from clinical to commercial manufacturing.
Velsori primary focus on development and manufacturing of glycoprotein pharmaceuticals against breast cancer, supplies KEP Taiwan with KEP-437 & KEP-438 for global clinical trials and commercialization in the future. Velsori offers the advanced technology and services to become the best partner for clients from clinical to commercial manufacturing.
Industry/Entity Type
Biotechnology
Requirements
Must have
- The new powerpoint design should based on our current logo.
Should not have
- The similar design with current powerpoint style. Please don't refer the design style of our current website http://www.velsori-example.com.tw/ as well, we will re-design it soon.

```html
<!DOCTYPE html>
<html lang="en">
<head>
<meta charset="utf-8">
<title>Velsori Biotech – Presentation Template</title>
<link href="https://fonts.googleapis.com/css2?family=Open+Sans:wght@300;400;600;700&display=swap" rel="stylesheet">
<style>
:root{
  --yellow:#f5c03a;
  --yellow-light:#f8d76e;
  --orange:#f5a122;
  --olive:#8c9d2c;
  --olive-dark:#5f7419;
  --title:#6e7f1e;
  --brand:#2c4a1e;
  --text:#555;
  --muted:#9a9a9a;
  --red:#e8452c;
  --leaf:#5e8a2a;
}
*{box-sizing:border-box;margin:0;padding:0}
html,body{width:1200px;height:1111px;overflow:hidden;background:#fff;font-family:"Open Sans",sans-serif;color:var(--text)}
.slide{position:absolute;width:383px;height:215px;background:#fff;overflow:hidden;box-shadow:0 1px 3px rgba(0,0,0,.18)}
.abs{position:absolute}
.photo{position:absolute}
.title{position:absolute;left:16px;top:14px;font-size:15px;font-weight:400;color:var(--title);line-height:1.2}
.title::after{content:"";display:block;width:24px;height:2px;background:var(--orange);margin-top:3px}
.brand{position:absolute;top:12px;right:14px;display:flex;align-items:center;gap:3px;font-size:10px;font-weight:700;letter-spacing:.6px;color:var(--brand)}
.brand .dot{width:7px;height:7px;border-radius:50%;background:var(--orange)}
.footer{position:absolute;left:0;right:0;bottom:0;height:8px;background:linear-gradient(90deg,var(--orange),var(--yellow) 55%,#b9c12c)}
.page{position:absolute;right:4px;bottom:1px;width:14px;height:14px;border-radius:50%;background:#fff;border:1.5px solid var(--olive);font-size:5px;font-weight:600;color:var(--olive);display:flex;align-items:center;justify-content:center}
.tiny{font-size:4.2px;line-height:1.5;color:var(--muted)}
.small{font-size:5.2px;line-height:1.55;color:var(--text)}
.label{font-size:6.4px;color:var(--olive-dark);font-weight:400}
.label.orange{color:var(--orange)}
.icon-sq{position:absolute;width:12px;height:12px;background:var(--yellow);border-radius:2px;display:flex;align-items:center;justify-content:center}
.icon-ci{position:absolute;width:14px;height:14px;border-radius:50%;background:var(--yellow);display:flex;align-items:center;justify-content:center}
.icon-ci.outline{background:#fff;border:1.5px solid #e6e6e6}
.we-are{font-size:6.8px;font-weight:600;color:#555}
.we-are b{color:var(--orange)}
.presenters{position:absolute;display:flex;align-items:flex-end;gap:12px}
.person{display:flex;align-items:flex-start;gap:3px}
.person .name{font-size:7px;color:#333;line-height:1}
.person .role{font-size:3.8px;color:#777}
.pre-label{font-size:3.4px;color:#999}
</style>
</head>
<body>

<svg width="0" height="0" style="position:absolute">
  <defs>
    <symbol id="user" viewBox="0 0 10 10"><circle cx="5" cy="3" r="2.3" fill="#555"/><path d="M1 10c0-3 2-4.5 4-4.5S9 7 9 10z" fill="#555"/></symbol>
    <symbol id="clock" viewBox="0 0 10 10"><circle cx="5" cy="5" r="3.6" fill="none" stroke="#fff" stroke-width="1"/><path d="M5 3v2.2l1.4 1" stroke="#fff" stroke-width="1" fill="none"/></symbol>
    <symbol id="tick" viewBox="0 0 10 10"><path d="M2.5 5.2l1.8 1.8 3.4-3.8" stroke="#fff" stroke-width="1.2" fill="none"/></symbol>
    <symbol id="search" viewBox="0 0 10 10"><circle cx="4.4" cy="4.4" r="2.3" fill="none" stroke="#fff" stroke-width="1"/><path d="M6 6l2 2" stroke="#fff" stroke-width="1.1"/></symbol>
    <symbol id="arrow" viewBox="0 0 10 10"><path d="M2 8L8 2M4 2h4v4" stroke="#fff" stroke-width="1.1" fill="none"/></symbol>
  </defs>
</svg>

<!-- 1 Cover -->
<section class="slide cover" style="left:8px;top:4px">
  <div class="photo" role="img" aria-label="Cupped hands holding soil with a young seedling, washed in yellow" style="inset:0;background:radial-gradient(circle at 50% 50%,#e7c24a 0,#f3c64c 35%,#f7cf5a 70%)"></div>
  <div class="abs" style="left:96px;top:90px;display:flex;align-items:center;gap:6px;font-size:32px;font-weight:700;letter-spacing:2px;color:var(--brand)"><span style="width:16px;height:16px;border-radius:50%;background:var(--orange)"></span>VELSORI</div>
</section>

<!-- 2 Title, oats -->
<section class="slide" style="left:408px;top:4px">
  <div class="photo" role="img" aria-label="Wooden scoop spilling rolled oats on white" style="left:0;top:0;width:383px;height:132px;background:linear-gradient(120deg,#f4efe4,#e9dcc0 45%,#f7f4ee)"></div>
  <div class="brand" style="top:14px">VELSORI</div>
  <div class="abs" style="left:0;top:132px;width:383px;height:40px;background:linear-gradient(90deg,var(--yellow-light),var(--yellow));text-align:center">
    <div style="font-size:15px;color:#3a3320;margin-top:6px">Your Title Goes Here</div>
    <div style="font-size:5px;color:#3a3320">Your Subtitle Goes Here</div>
  </div>
  <div class="presenters" style="left:14px;top:179px">
    <div><div class="pre-label">Presented by:</div>
      <div class="person"><svg width="8" height="8"><use href="#user"/></svg><div><div class="name">Lena Marsh</div><div class="role">VP Marketing</div></div></div></div>
    <div class="person"><svg width="8" height="8"><use href="#user"/></svg><div><div class="name">Tara Quill</div><div class="role">Senior Consultant</div></div></div>
    <div style="width:1px;height:20px;background:#bbb;margin:0 8px"></div>
    <div><div class="pre-label">Presented for:</div>
      <div class="person"><svg width="8" height="8"><use href="#user"/></svg><div><div class="name">Owen Pratt</div><div class="role">Vice President</div></div></div></div>
  </div>
  <div class="abs" style="left:0;bottom:0;width:383px;height:9px;background:linear-gradient(90deg,var(--orange),var(--yellow))"></div>
  <div class="abs" style="left:6px;bottom:2px;font-size:3.4px;color:#fff">© 2016 Velsori Biotech. All rights reserved.</div>
  <div class="abs" style="right:16px;bottom:0;width:62px;height:9px;background:#fff;font-size:3.6px;color:#666;text-align:center;line-height:9px">November 30, 2016</div>
  <div class="abs" style="right:0;bottom:0;width:14px;height:9px;background:#8aae2e"></div>
</section>

<!-- 3 Title, building -->
<section class="slide" style="left:808px;top:4px">
  <div class="abs" style="left:24px;top:24px;font-size:12px;font-weight:700;letter-spacing:.6px;color:var(--brand)">VELSORI</div>
  <div class="photo" role="img" aria-label="Modern office building facade under a blue sky" style="left:0;top:28px;width:383px;height:110px;background:linear-gradient(100deg,#6e8db3 0,#b9c6d4 35%,#dfe3e6 60%,#9fb2c7)"></div>
  <div class="abs" style="left:0;top:138px;width:383px;height:40px;text-align:center;background:#fff">
    <div style="font-size:14px;color:#3a3a3a;margin-top:6px">Your Title Goes Here</div>
    <div style="font-size:4.8px;color:#444">Your Subtitle Goes Here</div>
  </div>
  <div class="abs" style="left:0;top:178px;width:383px;height:10px;background:linear-gradient(180deg,#9cb83a,#d8c64a)"></div>
  <div class="presenters" style="left:6px;top:198px;gap:8px">
    <div class="pre-label">Presented by:</div>
    <div class="person"><svg width="6" height="6"><use href="#user"/></svg><div><div class="name" style="font-size:4.6px">Lena Marsh</div><div class="role" style="font-size:2.8px">VP Marketing</div></div></div>
    <div class="person"><svg width="6" height="6"><use href="#user"/></svg><div><div class="name" style="font-size:4.6px">Tara Quill</div><div class="role" style="font-size:2.8px">Senior Consultant</div></div></div>
    <div style="width:1px;height:11px;background:#bbb;margin:0 12px"></div>
    <div class="pre-label">Presented for:</div>
    <div class="person"><svg width="6" height="6"><use href="#user"/></svg><div><div class="name" style="font-size:4.6px">Owen Pratt</div><div class="role" style="font-size:2.8px">Vice President</div></div></div>
  </div>
  <div class="abs" style="right:12px;top:203px;font-size:4px;color:#666">Cityname | November 30, 2016</div>
</section>

<!-- 4 Agenda -->
<section class="slide" style="left:8px;top:226px">
  <div class="title">Our Agenda</div>
  <div class="brand"><span class="dot"></span>VELSORI</div>
  <div class="agenda">
    <div class="icon-sq" style="left:58px;top:60px"><svg width="9" height="9"><use href="#clock"/></svg></div>
    <div class="abs" style="left:76px;top:58px;width:110px"><div class="label">Agenda One</div><div class="tiny">10:00</div><div class="tiny">Opening words and an outline of the session ahead.</div></div>
    <div class="icon-sq" style="left:58px;top:104px"><svg width="9" height="9"><use href="#clock"/></svg></div>
    <div class="abs" style="left:76px;top:102px;width:110px"><div class="label">Agenda Two</div><div class="tiny">11:00</div><div class="tiny">A short review of our platform and recent results.</div></div>
    <div class="icon-sq" style="left:58px;top:148px"><svg width="9" height="9"><use href="#clock"/></svg></div>
    <div class="abs" style="left:76px;top:146px;width:110px"><div class="label">Agenda Three</div><div class="tiny">12:00</div><div class="tiny">Quality systems and our manufacturing capacity.</div></div>
    <div class="icon-sq" style="left:213px;top:60px"><svg width="9" height="9"><use href="#clock"/></svg></div>
    <div class="abs" style="left:231px;top:58px;width:110px"><div class="label">Agenda Four</div><div class="tiny">13:00</div><div class="tiny">Client projects and how we support each stage.</div></div>
    <div class="icon-sq" style="left:213px;top:104px"><svg width="9" height="9"><use href="#clock"/></svg></div>
    <div class="abs" style="left:231px;top:102px;width:110px"><div class="label">Agenda Five</div><div class="tiny">14:00</div><div class="tiny">Timelines, milestones and the road to launch.</div></div>
    <div class="icon-sq" style="left:213px;top:148px"><svg width="9" height="9"><use href="#clock"/></svg></div>
    <div class="abs" style="left:231px;top:146px;width:110px"><div class="label">Agenda Six</div><div class="tiny">15:00</div><div class="tiny">Questions, discussion and closing remarks.</div></div>
  </div>
  <div class="footer"></div><div class="page">4</div>
</section>

<!-- 5 Services -->
<section class="slide" style="left:408px;top:226px">
  <div class="title">Our Services</div>
  <div class="brand"><span class="dot"></span>VELSORI</div>
  <div class="photo" role="img" aria-label="Open hand holding soil with a green sprout" style="left:35px;top:50px;width:150px;height:94px;background:linear-gradient(135deg,#f3ede6,#d9b9a0 50%,#5a4a35 62%,#f1ece6)"></div>
  <div class="abs" style="left:35px;top:152px;width:150px"><div class="label orange" style="font-size:5.6px">Your Title Goes Here</div><div class="tiny">We take each product from cell line to filled vial with care, clear reports and strict quality control at every step of the way.</div></div>
  <div class="icon-ci" style="left:210px;top:52px"><svg width="9" height="9"><use href="#tick"/></svg></div>
  <div class="abs" style="left:232px;top:50px;width:128px"><div class="label" style="font-size:5.6px">Service Number One</div><div class="tiny">Process development for cell lines, media and purification, built to scale cleanly.</div></div>
  <div class="icon-ci" style="left:210px;top:97px"><svg width="9" height="9"><use href="#arrow"/></svg></div>
  <div class="abs" style="left:232px;top:95px;width:128px"><div class="label" style="font-size:5.6px">Service Number Two</div><div class="tiny">Clinical supply under cGMP, with batch records and release testing on site.</div></div>
  <div class="icon-ci" style="left:210px;top:143px"><svg width="9" height="9"><use href="#search"/></svg></div>
  <div class="abs" style="left:232px;top:141px;width:128px"><div class="label" style="font-size:5.6px">Service Number One</div><div class="tiny">Commercial manufacturing with steady capacity and full regulatory support.</div></div>
  <div class="footer"></div><div class="page">5</div>
</section>

<!-- 6 About -->
<section class="slide" style="left:808px;top:226px">
  <div class="photo" role="img" aria-label="Hand lifting a green seedling with soil against a pale blue sky" style="left:0;top:0;width:267px;height:207px;background:linear-gradient(160deg,#a9c9e6,#d9e8f2 45%,#9a8a6a 75%,#e9d6c5)"></div>
  <div class="brand"><span class="dot"></span>VELSORI</div>
  <div class="abs" style="left:192px;top:45px;width:191px;height:121px;background:linear-gradient(135deg,rgba(168,176,40,.92),rgba(140,157,44,.92));padding:14px 16px">
    <div style="font-size:14px;color:#f3f0b0">About Us</div>
    <div style="width:22px;height:2px;background:var(--orange);margin:2px 0 8px"></div>
    <div class="tiny" style="color:#fff">We are a contract development and manufacturing team for biologics, serving clients from first trials to market.</div>
    <div class="tiny" style="color:#fff;margin-top:4px">Our staff bring years of hands-on work in glycoprotein medicine.</div>
  </div>
  <div class="footer"></div><div class="page">6</div>
</section>

<!-- 7 Quote -->
<section class="slide" style="left:8px;top:448px">
  <div class="title">Quote Area</div>
  <div class="brand"><span class="dot"></span>VELSORI</div>
  <div class="photo" role="img" aria-label="Seedling in soil under warm green light" style="left:0;top:47px;width:192px;height:133px;background:linear-gradient(135deg,#a3b23a,#7e9a33 55%,#b4c04a)"></div>
  <div class="photo" role="img" aria-label="Laboratory bioreactor vessel with measurement markings" style="left:192px;top:47px;width:191px;height:133px;background:linear-gradient(90deg,#9aa590,#cfd8cf 40%,#b8e0b0 70%,#8fa28a)"></div>
  <div class="abs" style="left:30px;top:86px;width:160px;font-size:7px;line-height:1.45;color:#fff">
    <span style="font-size:10px;line-height:0">“</span> Coming together is a beginning.<br>Keeping together is progress.<br>Working together is success. <span style="font-size:10px;line-height:0">”</span>
    <div style="font-size:4.5px;margin-top:8px">- Elias Corvin -</div>
  </div>
  <div class="footer"></div><div class="page">7</div>
</section>

<!-- 8 Text Area -->
<section class="slide" style="left:408px;top:448px">
  <div class="title">Text Area</div>
  <div class="brand"><span class="dot"></span>VELSORI</div>
  <div class="abs" style="left:33px;top:70px;width:325px">
    <div class="we-are">We are <b>Velsori</b> Biotech</div>
    <div class="small" style="font-size:4.8px;color:#777;margin-top:14px">We develop and manufacture biologics with care, from early clinical supply to commercial scale, under strict quality control and clear reporting so each client can plan with confidence.</div>
    <div class="small" style="font-size:4.8px;color:#777;margin-top:6px">Our facility runs modern single-use lines and a trained team that keeps every batch on schedule and in line with global standards.</div>
    <div class="small" style="font-size:4.8px;color:#777;margin-top:6px">We aim to be a steady long-term partner for every project we take on.</div>
  </div>
  <div class="footer"></div><div class="page">8</div>
</section>

<!-- 9 Vision & Mission -->
<section class="slide" style="left:808px;top:448px">
  <div class="title">Our Vision &amp; Mission</div>
  <div class="brand"><span class="dot"></span>VELSORI</div>
  <div class="photo" role="img" aria-label="Seedling in cupped hands on an olive green background" style="left:0;top:47px;width:383px;height:138px;background:radial-gradient(circle at 50% 60%,#9aa637,#b0b83d 40%,#a3ad36 80%)"></div>
  <div class="abs" style="left:24px;top:62px;width:170px;color:#fff">
    <div style="font-size:8.5px;color:#f7f0b0">• Our Vision:</div>
    <div style="font-size:7px;font-weight:600;line-height:1.35;margin-top:2px">Go to the Next Level<br>Without look in the past</div>
    <div class="tiny" style="color:#fff;margin-top:10px">We want to lead in glycoprotein manufacturing by pairing sound science with careful, reliable work for clients around the world.</div>
  </div>
  <div class="abs" style="left:215px;top:62px;width:155px;color:#fff">
    <div style="font-size:8.5px;color:#f7f0b0">• Our Missions:</div>
    <div style="display:flex;gap:6px;margin-top:5px"><div class="icon-ci outline" style="position:static;flex:none"></div><div><div style="font-size:4.6px">Your Text Here</div><div class="tiny" style="color:#fff">Deliver safe products on time.</div></div></div>
    <div style="display:flex;gap:6px;margin-top:6px"><div class="icon-ci outline" style="position:static;flex:none"></div><div><div style="font-size:4.6px">Your Text Here</div><div class="tiny" style="color:#fff">Keep quality first in every step.</div></div></div>
    <div style="display:flex;gap:6px;margin-top:6px"><div class="icon-ci outline" style="position:static;flex:none"></div><div><div style="font-size:4.6px">Your Text Here</div><div class="tiny" style="color:#fff">Grow with our clients and staff.</div></div></div>
  </div>
  <div class="footer"></div><div class="page">9</div>
</section>

<!-- 10 Text Area framed -->
<section class="slide" style="left:8px;top:670px;background:linear-gradient(90deg,var(--orange) 50%,var(--yellow) 50%)">
  <div class="abs" style="left:14px;top:14px;width:355px;height:187px;background:#fff"></div>
  <div class="title" style="left:32px;top:32px">Text Area</div>
  <div class="brand" style="top:30px;right:26px"><span class="dot"></span>VELSORI</div>
  <div class="abs" style="left:32px;top:78px;width:320px">
    <div class="we-are">We are <b>Velsori</b> Biotech</div>
    <div class="tiny" style="margin-top:8px;font-size:4.4px">We develop and manufacture biologics with care, from early clinical supply to commercial scale, under strict quality control and clear reporting for every client.</div>
    <div class="tiny" style="margin-top:5px;font-size:4.4px">Our facility runs modern single-use lines and a trained team that keeps every batch on schedule and in line with global standards.</div>
    <div class="tiny" style="margin-top:5px;font-size:4.4px">We aim to be a steady long-term partner for every project we take on, with open talks and honest timelines from start to finish.</div>
  </div>
</section>

<!-- 11 Title with two points -->
<section class="slide" style="left:408px;top:670px">
  <div class="photo" role="img" aria-label="Person in a white shirt holding dark soil in both hands" style="left:0;top:0;width:192px;height:207px;background:linear-gradient(180deg,#f1f1f1,#e4e4e4 45%,#4a3b2c 62%,#d8cfc5)"></div>
  <div class="abs" style="left:0;top:121px;width:192px;height:70px;background:rgba(160,170,40,.82);display:flex;align-items:center;justify-content:center;font-size:16px;font-weight:700;letter-spacing:1px;color:var(--brand)">VELSORI</div>
  <div class="brand"><span class="dot"></span>VELSORI</div>
  <div class="title" style="left:210px;top:58px;font-size:13.5px">Your Title Goes Here</div>
  <div class="abs" style="left:210px;top:92px;width:150px;display:flex;gap:8px"><div style="flex:none;width:11px;height:11px;border-radius:50%;background:#1f3a1a;color:#fff;font-size:5px;display:flex;align-items:center;justify-content:center">1</div><div><div style="font-size:5.4px;color:#444">Your Text Goes Here</div><div class="tiny">Clear steps from first contact to signed supply plan.</div></div></div>
  <div class="abs" style="left:210px;top:144px;width:150px;display:flex;gap:8px"><div style="flex:none;width:11px;height:11px;border-radius:50%;background:#1f3a1a;color:#fff;font-size:5px;display:flex;align-items:center;justify-content:center">2</div><div><div style="font-size:5.4px;color:#444">Your Text Goes Here</div><div class="tiny">Steady batches, open data and support at each stage.</div></div></div>
  <div class="footer"></div><div class="page">11</div>
</section>

<!-- 12 Photo collage -->
<section class="slide" style="left:808px;top:670px">
  <div class="photo" role="img" aria-label="Scoop of oats tinted yellow green" style="left:5px;top:5px;width:123px;height:95px;background:linear-gradient(135deg,#d9d25a,#a9b43a)"></div>
  <div class="abs" style="left:22px;top:45px;font-size:13px;font-weight:700;letter-spacing:1px;color:#fff">VELSORI</div>
  <div class="photo" role="img" aria-label="Scientist looking into a microscope" style="left:5px;top:106px;width:123px;height:92px;background:linear-gradient(135deg,#c8d2dc,#7c8a98 50%,#e8ecef)"></div>
  <div class="photo" role="img" aria-label="Open hands under a glowing digital panel on a teal background" style="left:134px;top:5px;width:131px;height:193px;background:radial-gradient(circle at 50% 45%,#9fdad6,#3e9aa0 55%,#1f6e78)"></div>
  <div class="brand"><span class="dot"></span>VELSORI</div>
  <div class="title" style="left:280px;top:36px;font-size:13.5px;line-height:1.1">Your Title<br>Goes Here</div>
  <div class="abs" style="left:280px;top:86px;width:92px">
    <div class="tiny" style="font-size:3.8px">We pair trained people with modern tools to bring new medicines to patients faster.</div>
    <div class="tiny" style="font-size:3.8px;margin-top:4px">Every batch is tested and released with full records.</div>
    <div class="tiny" style="font-size:3.8px;margin-top:4px">Our labs support both early studies and late scale work.</div>
  </div>
  <div class="footer"></div><div class="page">12</div>
</section>

<!-- 13 Portfolio -->
<section class="slide" style="left:8px;top:892px">
  <div class="title">Portfolio Area</div>
  <div class="abs" style="left:20px;top:43px;width:160px">
    <div style="font-size:6px;color:var(--orange)">Heading Goes Here</div>
    <div class="tiny" style="font-size:3.8px">A short look at the projects we have carried from early research through to steady supply.</div>
  </div>
  <div class="icon-ci" style="left:30px;top:79px"><svg width="9" height="9"><use href="#search"/></svg></div>
  <div class="abs" style="left:52px;top:79px;width:105px"><div style="font-size:5.2px;color:var(--olive-dark)">Your Text Here</div><div class="tiny" style="font-size:3.6px">Research and early process design.</div></div>
  <div class="icon-ci" style="left:30px;top:106px"><svg width="9" height="9"><use href="#arrow"/></svg></div>
  <div class="abs" style="left:52px;top:106px;width:105px"><div style="font-size:5.2px;color:var(--olive-dark)">Your Text Here</div><div class="tiny" style="font-size:3.6px">Scale-up and pilot clinical lots.</div></div>
  <div class="icon-ci" style="left:30px;top:134px"><svg width="9" height="9"><use href="#tick"/></svg></div>
  <div class="abs" style="left:52px;top:134px;width:105px"><div style="font-size:5.2px;color:var(--olive-dark)">Your Text Here</div><div class="tiny" style="font-size:3.6px">Release testing and quality review.</div></div>
  <div class="icon-ci" style="left:30px;top:161px"><svg width="9" height="9"><use href="#clock"/></svg></div>
  <div class="abs" style="left:52px;top:161px;width:105px"><div style="font-size:5.2px;color:var(--olive-dark)">Your Text Here</div><div class="tiny" style="font-size:3.6px">Commercial supply on a set plan.</div></div>
  <div class="photo" role="img" aria-label="Person in white holding soil, split into four panels" style="left:192px;top:8px;width:181px;height:192px;background:linear-gradient(180deg,#f2f2f2,#e2e2e2 50%,#5a4838 68%,#e6ddd3)"></div>
  <div class="abs" style="left:282px;top:8px;width:1.5px;height:192px;background:#fff"></div>
  <div class="abs" style="left:192px;top:103px;width:181px;height:1.5px;background:#fff"></div>
  <div class="footer"></div><div class="page">13</div>
</section>

<!-- 14 Tiles -->
<section class="slide" style="left:408px;top:892px">
  <div class="title">Your Title Goes Here</div>
  <div class="brand"><span class="dot"></span>VELSORI</div>
  <div class="photo" role="img" aria-label="Hand holding soil with a small plant" style="left:27px;top:54px;width:108px;height:63px;background:linear-gradient(135deg,#f2ede6,#c9a88d 55%,#f3efe9)"></div>
  <div class="abs" style="left:138px;top:54px;width:108px;height:63px;background:var(--orange);padding:8px 9px;color:#fff"><div style="font-size:5.4px">Heading Goes Here</div><div class="tiny" style="color:#fff;font-size:3.7px;margin-top:4px">Short note on our process, quality checks and delivery standards.</div></div>
  <div class="photo" role="img" aria-label="Green shoots growing through snow" style="left:249px;top:54px;width:108px;height:63px;background:linear-gradient(180deg,#f6f6f6,#dfe7d6 60%,#a6c071)"></div>
  <div class="abs" style="left:27px;top:120px;width:108px;height:63px;background:var(--leaf);padding:8px 9px;color:#fff"><div style="font-size:5.4px">Heading Goes Here</div><div class="tiny" style="color:#fff;font-size:3.7px;margin-top:4px">Short note on our process, quality checks and delivery standards.</div></div>
  <div class="photo" role="img" aria-label="Wooden scoop of red beans scattered on white" style="left:138px;top:120px;width:108px;height:63px;background:linear-gradient(135deg,#f4f1ed,#9a5b47 55%,#f1ece8)"></div>
  <div class="abs" style="left:249px;top:120px;width:108px;height:63px;background:var(--red);padding:8px 9px;color:#fff"><div style="font-size:5.4px">Heading Goes Here</div><div class="tiny" style="color:#fff;font-size:3.7px;margin-top:4px">Short note on our process, quality checks and delivery standards.</div></div>
  <div class="footer"></div><div class="page">14</div>
</section>

<!-- 15 Text with beans -->
<section class="slide" style="left:808px;top:892px">
  <div class="title">Your Title Goes Here</div>
  <div class="brand"><span class="dot"></span>VELSORI</div>
  <div class="abs" style="left:30px;top:70px;width:140px">
    <div class="we-are">We are <b>Velsori</b> Biotech</div>
    <div class="tiny" style="margin-top:14px">We develop and manufacture biologics with care, from early clinical supply to commercial scale, under strict quality control.</div>
    <div class="tiny" style="margin-top:5px">Each project gets clear plans, honest timelines and steady support from our team.</div>
  </div>
  <div class="photo" role="img" aria-label="Scoop of red beans" style="left:190px;top:84px;width:56px;height:72px;background:linear-gradient(160deg,#f3efea,#8a4a3a 60%,#f2ede8)"></div>
  <div class="photo" role="img" aria-label="Wooden scoop with red beans" style="left:254px;top:84px;width:56px;height:72px;background:linear-gradient(200deg,#f3efea,#c49a70 45%,#8a4a3a 70%,#f2ede8)"></div>
  <div class="photo" role="img" aria-label="Red beans scattered on white" style="left:318px;top:84px;width:56px;height:72px;background:linear-gradient(180deg,#f5f2ee,#a0604c 55%,#f2ede8)"></div>
  <div class="footer"></div><div class="page">15</div>
</section>

</body>
</html>
```